Website for "Bright Meadow Ltd" cleaning bsuiness

We require a website to expose our business to the local market. We want to provide background on who we are and what we do but in an easily digestible way. We clean domestic and commercial premises and want to provide a list of all of our services to potential customers. We operate out of Warrington in the UK.

We would like the website to be animated in some way so that the experience of using it is not dull or mundane. This website needs to be an extension of our company.

Target Market(s)

30 - 60 year olds for Domestic plus commercial clients

Industry/Entity Type

Cleaning Service

Coding

Coded - Design and coding required

Number of Pages Required

4 page

Font styles to use
Sans Serif

Colors
0455a3
3176b5
85acd3
cfdeed
ffffff
000000
1b1b1b
c8c8c8
757575

Requirements
Must have
• Logo which has been provided. Theme based around the logo and its colours. Simple layout to avoid confusion.
Nice to have
• Animations where possible to impress the customer.
Should not have
• any pictures of cleaning equipment, fairies, maids etc

```html
<!DOCTYPE html>
<html lang="en">
<head>
<meta charset="utf-8">
<title>Bright Meadow Ltd – Cleaning Service</title>
<link href="https://fonts.googleapis.com/css2?family=Open+Sans:wght@400;600;700;800&display=swap" rel="stylesheet">
<style>
  :root {
    --brand-deep: #0455a3;
    --brand: #3176b5;
    --brand-soft: #85acd3;
    --brand-pale: #cfdeed;
    --white: #ffffff;
    --black: #000000;
    --ink: #1b1b1b;
    --navy: #0d2b55;
    --grey-light: #c8c8c8;
    --grey: #757575;
    --hero-bg: #eeeeee;
  }
  * { box-sizing: border-box; margin: 0; padding: 0; }
  html, body {
    width: 1124px; height: 1200px; overflow: hidden;
    background: var(--white);
    font-family: "Open Sans", Arial, sans-serif;
  }
  .page { position: relative; width: 1124px; height: 1200px; overflow: hidden; }

  /* Header */
  .brand {
    position: absolute; left: 90px; top: 30px;
    display: flex; align-items: center; gap: 10px;
  }
  .brand__mark { width: 28px; height: 28px; background: var(--brand-deep); }
  .brand__name { font-size: 24px; font-weight: 700; color: var(--brand-deep); letter-spacing: -0.3px; }

  .social { position: absolute; left: 936px; top: 20px; display: flex; gap: 2px; }
  .social__item { width: 22px; height: 22px; display: block; }
  .social__item--a { background: #3b5998; }
  .social__item--b { background: #2f9ad8; }
  .social__item--c { background: #0e76a8; }
  .social__item--d { background: #dc4a38; }

  .phone {
    position: absolute; left: 815px; top: 52px;
    display: flex; align-items: center; gap: 12px;
    font-size: 22px; font-weight: 600; color: var(--navy);
  }
  .phone svg { width: 26px; height: 24px; }

  /* Hero */
  .hero { position: absolute; left: 0; top: 124px; width: 1124px; height: 460px; background: var(--hero-bg); }
  .hero__photo {
    position: absolute; left: 0; top: 0; width: 520px; height: 460px;
    background: radial-gradient(ellipse at 45% 45%, #f3f3f3 0%, #e8e6e6 55%, #e2e2e2 100%);
  }
  .nav {
    position: absolute; left: 171px; top: 104px; width: 779px; height: 49px;
    background: var(--brand); display: flex; padding-left: 150px; z-index: 3;
  }
  .nav__link {
    display: flex; align-items: center; height: 49px; padding: 0 28px;
    color: var(--white); font-size: 15px; text-decoration: none;
  }
  .nav__link--active { background: var(--brand-deep); padding: 0 27px; }

  .slider-dots { position: absolute; left: 1018px; top: 200px; display: flex; flex-direction: column; gap: 5px; }
  .slider-dots span { width: 12px; height: 12px; border-radius: 50%; background: #a9a9a9; }
  .slider-dots span.is-active { background: #666666; }

  .hero__title {
    position: absolute; left: 574px; top: 228px;
    font-size: 58px; font-weight: 800; line-height: 1; color: var(--brand-deep); letter-spacing: 1px;
  }
  .hero__subtitle {
    position: absolute; left: 572px; top: 298px;
    font-size: 50px; font-weight: 600; line-height: 1; color: var(--grey); letter-spacing: 29px;
  }
  .hero__rule { position: absolute; left: 574px; top: 369px; width: 456px; height: 1px; background: #bdbdbd; }
  .hero__text {
    position: absolute; left: 573px; top: 391px; width: 460px;
    font-size: 13px; line-height: 19.5px; color: var(--grey);
  }
  .hero__text a { color: var(--brand); font-weight: 700; text-decoration: none; }

  /* Welcome */
  .welcome-wave { position: absolute; left: 0; top: 460px; width: 1124px; height: 520px; }
  .welcome__photo {
    position: absolute; left: 120px; top: 596px; width: 260px; height: 384px;
    background: radial-gradient(ellipse at 50% 40%, #5a9ad8 0%, #3f82c2 45%, var(--brand) 80%);
  }
  .welcome__title {
    position: absolute; left: 412px; top: 590px;
    font-size: 62px; font-weight: 800; color: var(--white); line-height: 1; letter-spacing: 0.5px;
  }
  .welcome__col {
    position: absolute; top: 687px;
    font-size: 11.6px; line-height: 20.9px; color: var(--white);
  }
  .welcome__col--left { left: 412px; width: 222px; }
  .welcome__col--right { left: 653px; width: 380px; }
  .btn-more {
    position: absolute; left: 572px; top: 888px; width: 137px; height: 35px;
    background: var(--white); color: var(--brand);
    font-size: 13px; font-weight: 700; display: flex; align-items: center; justify-content: center;
    text-decoration: none;
  }

  /* Services */
  .services__title {
    position: absolute; left: 0; width: 1124px; top: 1048px; text-align: center;
    font-size: 35px; font-weight: 700; color: var(--brand);
  }
  .services__divider { position: absolute; left: 396px; top: 1102px; width: 326px; height: 18px; }
  .tabs { position: absolute; left: 332px; top: 1151px; display: flex; }
  .tab {
    height: 40px; display: flex; align-items: center; justify-content: center;
    font-size: 13px; font-weight: 600; position: relative;
  }
  .tab--active { width: 227px; background: var(--ink); color: var(--white); }
  .tab--active::after {
    content: ""; position: absolute; left: 110px; bottom: -6px;
    border-left: 6px solid transparent; border-right: 6px solid transparent; border-top: 6px solid var(--ink);
  }
  .tab--idle { width: 230px; background: var(--grey-light); color: var(--ink); }
</style>
</head>
<body>
<div class="page">

  <header>
    <div class="brand">
      <span class="brand__mark"></span>
      <span class="brand__name">Bright Meadow Ltd</span>
    </div>
    <div class="social" aria-label="Social links">
      <span class="social__item social__item--a"></span>
      <span class="social__item social__item--b"></span>
      <span class="social__item social__item--c"></span>
      <span class="social__item social__item--d"></span>
    </div>
    <div class="phone">
      <svg viewBox="0 0 26 24" aria-hidden="true">
        <path d="M2 9c0-4 5-6 11-6s11 2 11 6v2h-5V8c-2-1-10-1-12 0v3H2z" fill="#0455a3"/>
        <path d="M6 12h14l3 10H3z" fill="#0455a3"/>
        <circle cx="13" cy="16.5" r="3" fill="#fff"/>
      </svg>
      <span>0044 - 1925 - 0173</span>
    </div>
  </header>

  <section class="hero">
    <div class="hero__photo" role="img" aria-label="Photo of a smiling cleaner holding a spray bottle and a microfibre duster"></div>
  </section>

  <nav class="nav">
    <a class="nav__link nav__link--active" href="#">Home</a>
    <a class="nav__link" href="#">About Us</a>
    <a class="nav__link" href="#">Services</a>
    <a class="nav__link" href="#">Contact Us</a>
  </nav>

  <div class="slider-dots"><span></span><span class="is-active"></span><span></span></div>
  <h1 class="hero__title">CLEANING</h1>
  <div class="hero__subtitle">SERVICE</div>
  <div class="hero__rule"></div>
  <p class="hero__text">Lorem ipsum dolor sit amet, consectetur adipiscing elit. Duis fringilla eros a interdum tincidunt. Suspendisse mollis ultrices neque, vitae laoreet lacus tempor id. Curabitur magna lorem, malesuada non lorem eget. <a href="#">[ More ]</a></p>

  <svg class="welcome-wave" viewBox="0 0 1124 520" preserveAspectRatio="none" aria-hidden="true">
    <path d="M0 114 Q562 10 1124 114 V519 H0 Z" fill="#3176b5"/>
  </svg>
  <div class="welcome__photo" role="img" aria-label="Photo of a blue canister vacuum cleaner"></div>
  <h2 class="welcome__title">WELCOME TO !</h2>
  <p class="welcome__col welcome__col--left">Lorem ipsum dolor sit amet, consectetur adipiscing elit. Duis fringilla eros a interdum tincidunt. Suspendisse mollis ultrices neque, vitae laoreet lacus tempor id. Curabitur magna lorem, malesuada non lorem eget. Pellentesque commodo dui vitae quam eleifend faucibus. Maecenas arcu nisl, sollicitudin at erat et, hendrerit semper enim.</p>
  <p class="welcome__col welcome__col--right">Vivamus a sem tempus, ultricies tortor a, placerat ipsum. Quisque eu volutpat nibh, ut porta leo. Sed eros arcu, interdum id sagittis eu, tincidunt vitae justo. Praesent id placerat massa. Integer aliquam et nibh a posuere. Vestibulum rutrum, leo ut gravida tincidunt, diam lorem lacinia risus, sed ornare lorem enim quis sapien. Ut in dignissim sapien. In suscipit turpis at condimentum consectetur.</p>
  <a class="btn-more" href="#">READ MORE</a>

  <h2 class="services__title">OUR SERVICES</h2>
  <svg class="services__divider" viewBox="0 0 326 18" aria-hidden="true">
    <line x1="0" y1="9" x2="150" y2="9" stroke="#bdbdbd" stroke-width="1"/>
    <line x1="176" y1="9" x2="326" y2="9" stroke="#bdbdbd" stroke-width="1"/>
    <polygon points="163,2 170,7 167.5,15 158.5,15 156,7" fill="#a9a9a9"/>
  </svg>
  <div class="tabs">
    <div class="tab tab--active">Domestic Services</div>
    <div class="tab tab--idle">Commercial Cleaning</div>
  </div>

</div>
</body>
</html>
```